Instagram background for quotes

We need a 1080x1080 background for instagram. I use the Phonto app to put text over the image.

We create motivating and inspiring messages for our followers on IG.

Our brands message is, "Mediocre thinking leads to mediocre results. Get Mission - Get Motivated - Get Moving
https://www.example-social.test/steel_resolve_co/

We would like to move away from the rustic look and have a gloss black background with the goal of using text that is cleaner to match the SR in the logo.

I see the design remaining fairly close to what it is now with the logo at the top. I like the quotes on this brand here, https://www.example-social.test/talkwithtycoons/?hl=en. I see this being built into our new background with the quotations being aggressive to match the wings in our logo.

Here is another brand we like - https://www.example-social.test/boomboomdrive/

I've attached the files I was given by the logo designer who has disappeared. I am hoping what is there will suffice.

Target Market(s)

24-34 year old males

Industry/Entity Type

Quotes

Colors
000000
ffffff

Requirements
Must have
• Provided Logo without text
Nice to have
• Aggressive looking quotes to match wings
• Watermark logo in background

```html
<!DOCTYPE html>
<html lang="en">
<head>
<meta charset="utf-8">
<title>SR Quote Background</title>
<link rel="stylesheet" href="https://fonts.googleapis.com/css2?family=Teko:wght@600&display=swap">
<style>
  :root {
    --ink: #000000;
    --paper: #ffffff;
    --watermark: #161616;
  }
  html, body {
    margin: 0;
    padding: 0;
    width: 1200px;
    height: 1200px;
    overflow: hidden;
    background: var(--ink);
  }
  .quote-canvas {
    position: relative;
    width: 1200px;
    height: 1200px;
    background: var(--ink);
    overflow: hidden;
  }
  .frame-art {
    position: absolute;
    inset: 0;
    width: 1200px;
    height: 1200px;
  }
  .frame-line {
    stroke: var(--paper);
    stroke-width: 6;
    fill: none;
    stroke-linecap: square;
  }
  .quote-mark {
    fill: var(--paper);
  }
  .brand-mark {
    position: absolute;
    top: 58px;
    left: 0;
    width: 1200px;
    text-align: center;
    font-family: "Teko", sans-serif;
    font-weight: 600;
    font-size: 150px;
    line-height: 150px;
    letter-spacing: 6px;
    color: var(--paper);
    margin: 0;
  }
  .brand-watermark {
    position: absolute;
    top: 360px;
    left: 0;
    width: 1200px;
    text-align: center;
    font-family: "Teko", sans-serif;
    font-weight: 600;
    font-size: 520px;
    line-height: 520px;
    letter-spacing: 20px;
    color: var(--watermark);
    margin: 0;
  }
</style>
</head>
<body>
  <main class="quote-canvas">
    <p class="brand-watermark" aria-hidden="true">SR</p>

    <svg class="frame-art" viewBox="0 0 1200 1200" aria-hidden="true">
      <!-- top edge, split around the brand mark -->
      <line class="frame-line" x1="59" y1="59" x2="358" y2="59"/>
      <line class="frame-line" x1="837" y1="59" x2="1141" y2="59"/>
      <!-- right edge, split around the closing quote -->
      <line class="frame-line" x1="1141" y1="59" x2="1141" y2="767"/>
      <line class="frame-line" x1="1141" y1="1011" x2="1141" y2="1141"/>
      <!-- bottom edge -->
      <line class="frame-line" x1="59" y1="1141" x2="1141" y2="1141"/>
      <!-- left edge, split around the opening quote -->
      <line class="frame-line" x1="59" y1="59" x2="59" y2="161"/>
      <line class="frame-line" x1="59" y1="406" x2="59" y2="1141"/>

      <!-- opening quote -->
      <polygon class="quote-mark" points="39,256 57,256 89,314 71,314"/>
      <polygon class="quote-mark" points="79,256 97,256 128,314 110,314"/>
      <!-- closing quote -->
      <polygon class="quote-mark" points="1101,856 1120,856 1089,917 1069,917"/>
      <polygon class="quote-mark" points="1137,856 1156,856 1125,917 1105,917"/>
    </svg>

    <h1 class="brand-mark">SR</h1>
  </main>
</body>
</html>
```